rk ironcraft business card metallic look

revamp the existing design but want card to have a metalic look to it

Target Market(s)

construction industry

Industry/Entity Type

constrction

Contact Information for Business Card

front of card RK Ironcraft, phone 4165550193, email rk.ironcraftt@veltrano.com and instagram account; rk_ironcraft_

Font styles to use
Other font styles liked:
• masculine

Colors

Designer to choose only greyscale colors for use in the design.

Requirements
Must have
• back side RK Ironcraft then a list of everything : Siding, ACM Panels, Standing Seam,Soffit, Fascia, Gutters,Metal,Alu,inum, Viynyl, Metal Roofs and roof repairs
Nice to have
• I would like to keep the look of the existing card with the metal grids on the front
Should not have
• Need a design in two days

```html
<!DOCTYPE html>
<html lang="en">
<head>
<meta charset="utf-8">
<title>RK Ironcraft – Business Card</title>
<link href="https://fonts.googleapis.com/css2?family=Montserrat:wght@500;600;700;800&display=swap" rel="stylesheet">
<style>
  :root {
    --canvas: #5c5c5c;
    --dark-card-hi: #5a5a5a;
    --dark-card: #3a3a3a;
    --dark-card-deep: #252525;
    --light-card-hi: #ffffff;
    --light-card: #efefef;
    --light-card-shade: #d9d9d9;
    --ink-dark: #151515;
    --ink-light: #f2f2f2;
    --dot: #9e9e9e;
  }
  * { box-sizing: border-box; margin: 0; padding: 0; }
  html, body {
    width: 1200px; height: 1200px; overflow: hidden;
    background: radial-gradient(ellipse at 50% 40%, #7a7a7a, var(--canvas) 60%, #3e3e3e);
    font-family: "Montserrat", sans-serif;
  }
  .sheet {
    width: 1200px; height: 1200px;
    display: flex; flex-direction: column; align-items: center; justify-content: center;
    gap: 52px;
  }
  .card {
    position: relative;
    width: 900px; height: 514px;
    border-radius: 6px;
    overflow: hidden;
    box-shadow: 0 4px 0 #1e1e1e, 0 8px 0 #2c2c2c, 0 18px 34px rgba(0,0,0,0.45);
  }
  .card-art { position: absolute; inset: 0; width: 100%; height: 100%; }
  .card-front {
    background:
      linear-gradient(115deg, rgba(255,255,255,0) 30%, rgba(255,255,255,0.08) 45%, rgba(255,255,255,0) 60%),
      linear-gradient(160deg, var(--dark-card-hi), var(--dark-card) 45%, var(--dark-card-deep));
  }
  .card-back {
    background:
      linear-gradient(115deg, rgba(255,255,255,0) 30%, rgba(255,255,255,0.7) 45%, rgba(255,255,255,0) 60%),
      linear-gradient(160deg, var(--light-card-hi), var(--light-card) 55%, var(--light-card-shade));
  }

  .brand-mark {
    position: absolute;
    left: 90px; top: 108px;
    display: flex; align-items: center; gap: 18px;
  }
  .brand-dot {
    width: 22px; height: 22px; border-radius: 50%;
    background: radial-gradient(circle at 35% 30%, #f2f2f2, #9a9a9a 55%, #3f3f3f);
    flex: none;
  }
  .brand-name {
    font-weight: 800;
    font-size: 62px;
    letter-spacing: 2px;
    text-transform: uppercase;
    line-height: 1;
  }
  .card-front .brand-name { color: var(--ink-light); }
  .card-back .brand-name { color: var(--ink-dark); }

  .contact-list {
    position: absolute; left: 90px; top: 222px;
    list-style: none;
    display: flex; flex-direction: column; gap: 20px;
  }
  .contact-item {
    display: flex; align-items: center; gap: 18px;
    color: var(--ink-light);
    font-weight: 500; font-size: 30px;
  }
  .contact-icon {
    width: 44px; height: 44px; border-radius: 50%;
    background: radial-gradient(circle at 35% 30%, #ececec, #8a8a8a 60%, #3c3c3c);
    box-shadow: 0 0 0 2px #1c1c1c;
    display: flex; align-items: center; justify-content: center;
    flex: none;
  }
  .contact-icon svg { width: 24px; height: 24px; }

  .service-list {
    position: absolute; left: 90px; top: 200px;
    list-style: none;
    display: flex; flex-direction: column; gap: 14px;
    color: var(--ink-dark);
    font-weight: 600; font-size: 25px; letter-spacing: 0.5px;
    text-transform: uppercase;
  }
  .service-list li { display: flex; align-items: center; gap: 10px; }
  .dot {
    width: 12px; height: 12px; border-radius: 50%;
    background: radial-gradient(circle at 35% 30%, #f0f0f0, var(--dot) 60%, #555);
    display: inline-block;
  }
</style>
</head>
<body>
<main class="sheet">

  <section class="card card-front" aria-label="Business card front">
    <svg class="card-art" viewBox="0 0 900 514" preserveAspectRatio="none" aria-hidden="true">
      <defs>
        <linearGradient id="frontWedge" x1="0" y1="0" x2="1" y2="0">
          <stop offset="0" stop-color="#7d7d7d"/>
          <stop offset="0.35" stop-color="#d6d6d6"/>
          <stop offset="0.6" stop-color="#8c8c8c"/>
          <stop offset="1" stop-color="#5c5c5c"/>
        </linearGradient>
        <linearGradient id="frontMetal" x1="0" y1="0" x2="1" y2="0.4">
          <stop offset="0" stop-color="#3a3a3a"/>
          <stop offset="0.25" stop-color="#b8b8b8"/>
          <stop offset="0.45" stop-color="#5e5e5e"/>
          <stop offset="0.7" stop-color="#d2d2d2"/>
          <stop offset="1" stop-color="#6a6a6a"/>
        </linearGradient>
      </defs>
      <polygon points="0,0 560,0 620,38 0,16" fill="url(#frontWedge)"/>
      <line x1="0" y1="16" x2="620" y2="38" stroke="#e6e6e6" stroke-width="1.5" opacity="0.7"/>
      <polygon points="0,16 620,38 600,44 0,26" fill="#1a1a1a" opacity="0.6"/>
      <polygon points="300,514 900,400 900,514" fill="#2a2a2a" opacity="0.8"/>
      <line x1="300" y1="514" x2="900" y2="400" stroke="#8a8a8a" stroke-width="1.5"/>
      <line x1="470" y1="470" x2="900" y2="380" stroke="#6a6a6a" stroke-width="1.5"/>
    </svg>
    <svg class="card-art" viewBox="0 0 900 514" preserveAspectRatio="none">
      <polygon role="img" aria-label="Corrugated brushed metal sheet" points="690,150 900,40 900,514 870,514" fill="url(#frontMetal)"/>
      <line x1="690" y1="150" x2="870" y2="514" stroke="#e8e8e8" stroke-width="2" opacity="0.8"/>
      <line x1="690" y1="150" x2="900" y2="40" stroke="#e8e8e8" stroke-width="2" opacity="0.8"/>
    </svg>

    <div class="brand-mark">
      <span class="brand-dot"></span>
      <h1 class="brand-name">RK Ironcraft</h1>
    </div>

    <ul class="contact-list">
      <li class="contact-item">
        <span class="contact-icon">
          <svg viewBox="0 0 24 24"><path d="M6.6 10.8a15 15 0 0 0 6.6 6.6l2.2-2.2a1 1 0 0 1 1-.25 11.4 11.4 0 0 0 3.6.57 1 1 0 0 1 1 1V20a1 1 0 0 1-1 1A17 17 0 0 1 3 4a1 1 0 0 1 1-1h3.5a1 1 0 0 1 1 1c0 1.25.2 2.45.57 3.57a1 1 0 0 1-.25 1z" fill="#1d1d1d"/></svg>
        </span>
        <span class="contact-text">416-555-0193</span>
      </li>
      <li class="contact-item">
        <span class="contact-icon">
          <svg viewBox="0 0 24 24"><rect x="3" y="6" width="18" height="12" rx="1.5" fill="none" stroke="#1d1d1d" stroke-width="2"/><path d="M3.5 7 12 13l8.5-6" fill="none" stroke="#1d1d1d" stroke-width="2"/></svg>
        </span>
        <span class="contact-text">rk.ironcraftt@veltrano.com</span>
      </li>
      <li class="contact-item">
        <span class="contact-icon"></span>
        <span class="contact-text">rk_ironcraft_</span>
      </li>
    </ul>
  </section>

  <section class="card card-back" aria-label="Business card back">
    <svg class="card-art" viewBox="0 0 900 514" preserveAspectRatio="none" aria-hidden="true">
      <defs>
        <linearGradient id="backWedge" x1="0" y1="0" x2="1" y2="0">
          <stop offset="0" stop-color="#a8a8a8"/>
          <stop offset="0.35" stop-color="#eeeeee"/>
          <stop offset="0.6" stop-color="#b0b0b0"/>
          <stop offset="1" stop-color="#8c8c8c"/>
        </linearGradient>
        <linearGradient id="backMetal" x1="0" y1="0" x2="1" y2="0.4">
          <stop offset="0" stop-color="#8e8e8e"/>
          <stop offset="0.25" stop-color="#f0f0f0"/>
          <stop offset="0.45" stop-color="#9c9c9c"/>
          <stop offset="0.7" stop-color="#e4e4e4"/>
          <stop offset="1" stop-color="#8a8a8a"/>
        </linearGradient>
      </defs>
      <polygon points="0,0 560,0 620,38 0,16" fill="url(#backWedge)"/>
      <polygon points="0,16 620,38 600,44 0,26" fill="#ffffff" opacity="0.85"/>
      <polygon points="300,514 900,400 900,514" fill="#e2e2e2"/>
      <line x1="300" y1="514" x2="900" y2="400" stroke="#8e8e8e" stroke-width="1.5"/>
      <line x1="470" y1="470" x2="900" y2="380" stroke="#a8a8a8" stroke-width="1.5"/>
    </svg>
    <svg class="card-art" viewBox="0 0 900 514" preserveAspectRatio="none">
      <polygon role="img" aria-label="Corrugated brushed metal sheet" points="690,150 900,40 900,514 870,514" fill="url(#backMetal)"/>
      <line x1="690" y1="150" x2="870" y2="514" stroke="#6e6e6e" stroke-width="2" opacity="0.7"/>
      <line x1="690" y1="150" x2="900" y2="40" stroke="#6e6e6e" stroke-width="2" opacity="0.7"/>
    </svg>

    <div class="brand-mark">
      <span class="brand-dot"></span>
      <h2 class="brand-name">RK Ironcraft</h2>
    </div>

    <ul class="service-list">
      <li>Siding <span class="dot"></span> ACM Panels <span class="dot"></span> Standing Seam</li>
      <li>Soffit <span class="dot"></span> Fascia <span class="dot"></span> Gutters <span class="dot"></span> Metal</li>
      <li>Aluminum <span class="dot"></span> Vinyl <span class="dot"></span> Metal Roof and</li>
      <li>Roofing Repairs</li>
    </ul>
  </section>

</main>
</body>
</html>
```